The Bright Lantern Studio Product Flyer for Trade Show

We are a small business that designs greeting cards/wall hangings. All our products are hand made using rolled strips of paper.
We are looking to showcase some of our card designs for a trade show this weekend. We want to include several of our images w/product number (on image or above/below), our business name, location and contact info and a brief description of our process. This will be for an 8.5"x11" single sided sheet of paper.

Target Market(s)

B2B Sales

Industry/Entity Type

Business

Font styles to use
Serif

Requirements
Must have
• Logo, Product Images w/numbers, Contact Info, Brief Description of process/pricing (.txt file), "10% off first order"
Nice to have
• Amazing color, sharp layout, even and professional appearance

```html
<!DOCTYPE html>
<html lang="en">
<head>
<meta charset="utf-8">
<title>The Bright Lantern Studio – Product Flyer</title>
<link href="https://fonts.googleapis.com/css2?family=Playfair+Display:wght@500;700;800&family=Source+Serif+4:wght@400;600;700&display=swap" rel="stylesheet">
<style>
  :root{
    --ink:#111111;
    --magenta:#e5097f;
    --leaf:#3f8a1f;
    --leaf-dark:#2e6b14;
    --lime:#c6dc3a;
    --lime-soft:#e3ef8a;
    --tag-border:#6bb02e;
    --badge:#ffe81a;
    --badge-edge:#f5c400;
    --badge-text:#d4141b;
    --label-grey:#9a9a9a;
    --footer:#1a6fb8;
    --footer-stripe:#48b2e6;
    --white:#ffffff;
  }
  *{box-sizing:border-box;margin:0;padding:0}
  html,body{width:848px;height:1200px;overflow:hidden}
  body{font-family:"Source Serif 4",Georgia,serif;background:#fff}
  .flyer{position:relative;width:848px;height:1200px;overflow:hidden}
  .backdrop{position:absolute;inset:0;
    background:
      radial-gradient(circle at 8% 10%,rgba(255,170,80,.55),transparent 22%),
      radial-gradient(circle at 92% 6%,rgba(255,150,190,.5),transparent 22%),
      radial-gradient(circle at 90% 55%,rgba(255,170,210,.45),transparent 30%),
      radial-gradient(circle at 10% 55%,rgba(120,210,240,.45),transparent 30%),
      radial-gradient(circle at 50% 85%,rgba(170,230,200,.45),transparent 35%),
      radial-gradient(circle at 50% 40%,rgba(255,250,200,.6),transparent 40%),
      #fbf6f4;}

  .brand-mark{position:absolute;left:78px;top:38px;width:124px;height:124px;border-radius:50%;background:var(--magenta)}
  .brand-name{position:absolute;left:294px;top:50px;font-family:"Playfair Display",Georgia,serif;line-height:1}
  .brand-name span{display:block}
  .brand-name .line-the,.brand-name .line-shop{font-size:44px;font-weight:500;color:var(--ink)}
  .brand-name .line-name{font-size:54px;font-weight:800;color:var(--magenta);margin:12px 0 10px}

  .tagline{position:absolute;left:118px;top:244px;width:680px;padding:6px 0;text-align:center;
    background:linear-gradient(90deg,transparent,var(--lime-soft) 20%,var(--lime-soft) 80%,transparent);
    color:var(--leaf-dark);font-weight:600;font-size:29px;line-height:1.22;text-transform:uppercase}

  .pricing{position:absolute;left:66px;top:366px;width:190px}
  .pricing-title{background:var(--leaf);color:var(--white);font-family:"Playfair Display",Georgia,serif;font-weight:700;font-size:25px;line-height:1.08;
    padding:8px 10px;clip-path:polygon(0 0,100% 0,88% 100%,0 100%);text-transform:uppercase}
  .pricing-line{margin-top:10px;background:var(--lime);color:var(--white);font-size:12.5px;line-height:1.25;
    padding:6px 10px;clip-path:polygon(0 0,100% 0,90% 100%,0 100%);width:168px}

  .card{position:absolute;width:150px;height:226px}
  .tag{position:absolute;left:0;top:0;width:150px;height:200px;transform:rotate(-8deg);transform-origin:50% 50%}
  .tag svg{position:absolute;inset:0;width:150px;height:200px}
  .card-art{position:absolute;left:22px;top:40px;width:106px;height:112px;border-radius:4px}
  .product-no{position:absolute;left:0;top:158px;width:150px;text-align:center;font-size:13px;font-weight:700;color:var(--leaf-dark);letter-spacing:.5px}
  .badge{position:absolute;left:-16px;top:142px;width:58px;height:58px;border-radius:50%;background:var(--badge);
    border:2px dashed var(--badge-edge);display:flex;flex-direction:column;align-items:center;justify-content:center;
    font-weight:700;color:var(--ink);line-height:.95}
  .badge .pct{font-size:18px}
  .badge .off{font-size:12px;color:var(--badge-text)}
  .first-order{position:absolute;left:-14px;top:208px;width:120px;height:18px;
    background:linear-gradient(90deg,var(--label-grey),rgba(154,154,154,.15));
    color:var(--white);font-size:12.5px;line-height:18px;padding-left:10px;text-transform:uppercase}

  .footer{position:absolute;left:0;top:1118px;width:848px;height:82px;background:var(--footer);
    border-bottom:10px solid var(--footer-stripe);color:var(--white);text-align:center;font-size:16px;line-height:1.35;padding-top:12px;letter-spacing:.3px}
</style>
</head>
<body>
<main class="flyer">
  <div class="backdrop" role="img" aria-label="Soft pastel watercolour wash with flower patterns in the corners"></div>

  <div class="brand-mark"></div>
  <h1 class="brand-name">
    <span class="line-the">THE</span>
    <span class="line-name">BRIGHT LANTERN</span>
    <span class="line-shop">STUDIO PRODUCT</span>
  </h1>

  <p class="tagline">All of our products are made with<br>hand-rolled strips of paper</p>

  <section class="pricing">
    <div class="pricing-title">Wholesale pricing is</div>
    <div class="pricing-line">4$ FOR 5"X7" CARDS &amp;</div>
    <div class="pricing-line">2.5$ FOR 4"X4" CARDS + SHIPPING.</div>
  </section>

  <svg width="0" height="0" style="position:absolute">
    <defs>
      <symbol id="tag-shape" viewBox="0 0 150 200">
        <path d="M10 34 Q10 20 24 20 L50 20 Q58 4 75 4 Q92 4 100 20 L126 20 Q140 20 140 34 L140 184 Q140 196 128 196 L22 196 Q10 196 10 184 Z"
              fill="#ffffff" stroke="#6bb02e" stroke-width="6"/>
        <circle cx="75" cy="17" r="5" fill="#e6e6e6" stroke="#bdbdbd"/>
      </symbol>
    </defs>
  </svg>

  <!-- Row 1 -->
  <article class="card" style="left:292px;top:363px">
    <div class="tag"><svg viewBox="0 0 150 200"><use href="#tag-shape"/></svg>
      <div class="card-art" role="img" aria-label="Quilled hummingbird with pink flower" style="background:linear-gradient(135deg,#c8ecd6,#f6c6dc)"></div>
      <p class="product-no">No. 101</p></div>
    <div class="badge"><span class="pct">10%</span><span class="off">OFF</span></div>
    <div class="first-order">First order</div>
  </article>
  <article class="card" style="left:477px;top:363px">
    <div class="tag"><svg viewBox="0 0 150 200"><use href="#tag-shape"/></svg>
      <div class="card-art" role="img" aria-label="Quilled green tree" style="background:linear-gradient(180deg,#4e9a3a,#8ccf5c 70%,#8a5a2b)"></div>
      <p class="product-no">No. 102</p></div>
    <div class="badge"><span class="pct">10%</span><span class="off">OFF</span></div>
    <div class="first-order">First order</div>
  </article>
  <article class="card" style="left:663px;top:363px">
    <div class="tag"><svg viewBox="0 0 150 200"><use href="#tag-shape"/></svg>
      <div class="card-art" role="img" aria-label="Colourful quilled elephant" style="background:linear-gradient(135deg,#2d4f8c,#7a3a8c,#2f8a4a)"></div>
      <p class="product-no">No. 103</p></div>
    <div class="badge"><span class="pct">10%</span><span class="off">OFF</span></div>
    <div class="first-order">First order</div>
  </article>

  <!-- Row 2 -->
  <article class="card" style="left:107px;top:606px">
    <div class="tag"><svg viewBox="0 0 150 200"><use href="#tag-shape"/></svg>
      <div class="card-art" role="img" aria-label="Quilled autumn maple leaves" style="background:linear-gradient(135deg,#f3c12b,#e0461e,#6a9a2a)"></div>
      <p class="product-no">No. 104</p></div>
    <div class="badge"><span class="pct">10%</span><span class="off">OFF</span></div>
    <div class="first-order">First order</div>
  </article>
  <article class="card" style="left:292px;top:606px">
    <div class="tag"><svg viewBox="0 0 150 200"><use href="#tag-shape"/></svg>
      <div class="card-art" role="img" aria-label="Quilled loon on water" style="background:linear-gradient(160deg,#f4f4f4,#3a3a3a 55%,#9fd8ea)"></div>
      <p class="product-no">No. 105</p></div>
    <div class="badge"><span class="pct">10%</span><span class="off">OFF</span></div>
    <div class="first-order">First order</div>
  </article>
  <article class="card" style="left:477px;top:606px">
    <div class="tag"><svg viewBox="0 0 150 200"><use href="#tag-shape"/></svg>
      <div class="card-art" role="img" aria-label="Quilled happy birthday lettering" style="background:linear-gradient(135deg,#f5f5f5,#a8dcc8,#e46a7a)"></div>
      <p class="product-no">No. 106</p></div>
    <div class="badge"><span class="pct">10%</span><span class="off">OFF</span></div>
    <div class="first-order">First order</div>
  </article>
  <article class="card" style="left:663px;top:606px">
    <div class="tag"><svg viewBox="0 0 150 200"><use href="#tag-shape"/></svg>
      <div class="card-art" role="img" aria-label="Colourful quilled butterfly" style="background:linear-gradient(135deg,#e8562a,#2a2a6a,#3aa0d8)"></div>
      <p class="product-no">No. 107</p></div>
    <div class="badge"><span class="pct">10%</span><span class="off">OFF</span></div>
    <div class="first-order">First order</div>
  </article>

  <!-- Row 3 -->
  <article class="card" style="left:107px;top:851px">
    <div class="tag"><svg viewBox="0 0 150 200"><use href="#tag-shape"/></svg>
      <div class="card-art" role="img" aria-label="Quilled state outline with red heart" style="background:linear-gradient(135deg,#f5f5f5,#5aa23a,#d0202a)"></div>
      <p class="product-no">No. 108</p></div>
    <div class="badge"><span class="pct">10%</span><span class="off">OFF</span></div>
    <div class="first-order">First order</div>
  </article>
  <article class="card" style="left:292px;top:851px">
    <div class="tag"><svg viewBox="0 0 150 200"><use href="#tag-shape"/></svg>
      <div class="card-art" role="img" aria-label="Quilled tropical fish with bubbles" style="background:linear-gradient(135deg,#f5f5f5,#3a78c8,#f2b22a)"></div>
      <p class="product-no">No. 109</p></div>
    <div class="badge"><span class="pct">10%</span><span class="off">OFF</span></div>
    <div class="first-order">First order</div>
  </article>
  <article class="card" style="left:477px;top:851px">
    <div class="tag"><svg viewBox="0 0 150 200"><use href="#tag-shape"/></svg>
      <div class="card-art" role="img" aria-label="Quilled dragonfly" style="background:linear-gradient(135deg,#f5f5f5,#2a6ac8,#8ccf3a)"></div>
      <p class="product-no">No. 110</p></div>
    <div class="badge"><span class="pct">10%</span><span class="off">OFF</span></div>
    <div class="first-order">First order</div>
  </article>
  <article class="card" style="left:663px;top:851px">
    <div class="tag"><svg viewBox="0 0 150 200"><use href="#tag-shape"/></svg>
      <div class="card-art" role="img" aria-label="Quilled tiered celebration cake with glasses" style="background:linear-gradient(180deg,#b48ad8,#f2a6a0 50%,#f5f5f5)"></div>
      <p class="product-no">No. 111</p></div>
    <div class="badge"><span class="pct">10%</span><span class="off">OFF</span></div>
    <div class="first-order">First order</div>
  </article>

  <footer class="footer">
    <p>CONTACT : XXXXXXXXXXXXXXXXX &nbsp;|&nbsp; LOCATION : 12 MAPLE ROW, MILLBROOK</p>
    <p>EMAIL.- XXXXXXXXXXXXXXXXXXXX | WWW.XXXXXXXXXXXX</p>
  </footer>
</main>
</body>
</html>
```